Real Estate - Property Management Business needs a Landlords Handbook designed

We need a landlord's handbook designed. We are a specialist property management business. The text and logos are there. The book needs images and to present more as a book. We would like to see designs that use orange, grey and white.
Our website is www.leasewisegroup.com.au to give you an idea of our brand.

Target Market(s)

Professional couples - property investors

Industry/Entity Type

Real Estate

Font styles to use
Sans Serif

Colors
ffffff
1b1b1b
f37122

Requirements
Must have
• Images of property owners and applicable images
Nice to have
• The Pembertons owner handbook is a guide to show you what I am looking for
Should not have
• This needs to look professional. No cartoon images

```html
<!DOCTYPE html>
<html lang="en">
<head>
<meta charset="utf-8">
<title>Our Team – LeaseWise Group Landlords Handbook</title>
<link href="https://fonts.googleapis.com/css2?family=Fira+Sans+Condensed:wght@600;700&family=Fira+Sans:wght@400;500;700&display=swap" rel="stylesheet">
<style>
  :root {
    --orange: #f37122;
    --ink: #1b1b1b;
    --white: #ffffff;
    --footer: #2c2f2f;
    --photo-a: #b9a58a;
    --photo-b: #2a2a2a;
  }
  * { margin: 0; padding: 0; box-sizing: border-box; }
  html, body { width: 851px; height: 1200px; overflow: hidden; background: var(--white); }
  .page {
    position: relative; width: 851px; height: 1200px; overflow: hidden;
    background: var(--white); color: var(--ink);
    font-family: "Fira Sans", Arial, sans-serif;
  }
  .page-title {
    position: absolute; left: 80px; top: 58px;
    font-family: "Fira Sans Condensed", "Arial Narrow", sans-serif;
    font-weight: 700; font-size: 72px; line-height: 1; color: var(--orange);
    letter-spacing: 0.5px;
  }
  .title-rule { position: absolute; left: 0; top: 132px; width: 851px; height: 10px; background: var(--orange); }

  .member-name {
    font-family: "Fira Sans Condensed", "Arial Narrow", sans-serif;
    font-weight: 700; font-size: 31px; line-height: 1.05; color: var(--orange);
  }
  .member-role {
    font-family: "Fira Sans Condensed", "Arial Narrow", sans-serif;
    font-weight: 600; font-size: 19px; line-height: 1.2; color: var(--orange);
    margin-top: 4px;
  }
  .bio p { font-size: 16px; text-align: justify; text-indent: 29px; }

  .photo-frame {
    border: 3px solid var(--orange); padding: 5px; background: var(--white);
  }
  .photo {
    width: 100%; height: 100%; border: 1px solid #ddd;
    background: linear-gradient(180deg, #f4f4f4 0%, #f4f4f4 25%, var(--photo-a) 45%, var(--photo-b) 100%);
  }

  .member-lead { position: absolute; left: 82px; top: 204px; width: 718px; }
  .member-lead .photo-frame { float: right; width: 226px; height: 333px; margin: 4px 0 6px 12px; }
  .member-lead .member-head { text-align: right; margin-bottom: 28px; }
  .member-lead .bio p { line-height: 22.5px; }
  .member-lead .bio p + p.spaced { margin-top: 22.5px; }

  .member-trust .photo-frame { position: absolute; left: 80px; top: 706px; width: 227px; height: 334px; }
  .member-trust .member-body { position: absolute; left: 318px; top: 704px; width: 484px; }
  .member-trust .member-head { margin-bottom: 30px; }
  .member-trust .bio p { line-height: 21px; }

  .footer-rule { position: absolute; left: 0; top: 1084px; width: 851px; height: 10px; background: var(--orange); }
  .footer { position: absolute; left: 0; top: 1094px; width: 851px; height: 106px; background: var(--footer); }
  .footer-url {
    position: absolute; left: 316px; top: 44px; font-size: 18px; color: var(--white); letter-spacing: 0.3px;
  }
  .footer-url .accent { color: var(--orange); }
  .brand {
    position: absolute; left: 656px; top: 36px; display: flex; align-items: center; gap: 7px;
  }
  .brand-mark { width: 14px; height: 14px; background: var(--orange); }
  .brand-name { font-family: "Fira Sans", Arial, sans-serif; font-weight: 700; font-size: 16px; color: var(--orange); }
  .page-tab {
    position: absolute; left: 796px; top: 1084px; width: 32px; height: 116px; background: var(--orange);
  }
  .page-number {
    position: absolute; left: 0; top: 56px; width: 32px; text-align: center;
    font-family: "Fira Sans Condensed", "Arial Narrow", sans-serif; font-weight: 700; font-size: 20px; color: var(--white);
  }
</style>
</head>
<body>
<main class="page">
  <h1 class="page-title">Our Team</h1>
  <div class="title-rule"></div>

  <section class="member-lead">
    <figure class="photo-frame"><div class="photo" role="img" aria-label="Portrait photo of Claire Hadley, Principal Licensee"></div></figure>
    <header class="member-head">
      <h2 class="member-name">Claire Hadley</h2>
      <p class="member-role">Principal Licensee</p>
    </header>
    <div class="bio">
      <p>Claire is the Director of Property Management for LeaseWise Group and has over 13 years experience in the property management industry. Committed to learning and extending her knowledge Claire has completed a Bachelor of Business Majoring in Marketing, a Certificate IV in Property Services (Real Estate) and is a licensed real estate agent.</p>
      <p class="spaced">Claire holds a reputation for consistently achieving excellent results within the dynamic areas of residential rental properties and portfolio management. It is her professional approach and strong focus on customer service that sets her apart. She is especially focused on building strong relationships with owners and tenants alike, building trust through clear and detailed communication, prompt follow-ups and a highly organised approach to client management.</p>
      <p>She enjoys the many challenges that she faces on a daily basis in her role and thrives on being able to help clients with all aspects of real estate. Claire is setting the bar when it comes to customer service in the property management industry.</p>
    </div>
  </section>

  <section class="member-trust">
    <figure class="photo-frame"><div class="photo" role="img" aria-label="Portrait photo of Megan Foster, Trust Account Administrator"></div></figure>
    <div class="member-body">
      <header class="member-head">
        <h2 class="member-name">Megan Foster</h2>
        <p class="member-role">Trust Account Administrator</p>
      </header>
      <div class="bio">
        <p>Qualified and experienced property professional having over 14 years experience in the real estate industry, making trust account management her specialty. Megan provides an unprecedented level of quality and professionalism. She feels privileged to be trusted with the responsibility of assisting clients to achieve their financial goals. Megan's extensive experience as well as being an investor herself enables her to service all clients to a higher level of understanding whilst being extremely attentive to detail. With an in-depth knowledge of all facets of property trust accounting, Megan understands what it takes to get the best possible outcome, focused on providing premium service in every instance.</p>
      </div>
    </div>
  </section>

  <div class="footer-rule"></div>
  <footer class="footer">
    <p class="footer-url">www.<span class="accent">leasewisegroup</span>.com.au</p>
    <div class="brand"><span class="brand-mark"></span><span class="brand-name">LeaseWise</span></div>
  </footer>
  <div class="page-tab"><span class="page-number">03</span></div>
</main>
</body>
</html>
```